Harborline Stay Collective Business Card Design

Design a business card for Harborline Stay Collective. Look at the website for colors and reference. Card should have logo, name, title, office number, mobile number, email, URL and a tagline like, "Luxury Hotel & Resort Email Marketing" (This might change).

https://www.harborlinestaycollective.net

The rest I will leave up to your imagination.

Contact Information for Business Card

Logo, name, title, office number, mobile number, email, URL and a tagline like, "Luxury Hotel & Resort Email Marketing" (This might change).

```html
<!DOCTYPE html>
<html lang="en">
<head>
<meta charset="utf-8">
<title>Harborline Stay Collective — Business Card</title>
<link rel="stylesheet" href="https://fonts.googleapis.com/css2?family=Jost:wght@400;600;700&family=Cormorant+Garamond:wght@400&display=swap">
<style>
  :root {
    --canvas: #c6c6c6;
    --card-black: #000000;
    --ink-white: #ffffff;
    --accent-orange: #f07a1a;
    --sea-teal: #1f8a8c;
    --forest-green: #3c5a34;
    --photo-shade: rgba(10, 20, 25, 0.35);
  }
  html, body {
    margin: 0;
    padding: 0;
    width: 1200px;
    height: 1000px;
    overflow: hidden;
    background: var(--canvas);
  }
  .sheet {
    position: relative;
    width: 1200px;
    height: 1000px;
    display: flex;
    align-items: center;
    justify-content: center;
    gap: 60px;
  }
  .card {
    position: relative;
    width: 525px;
    height: 300px;
    overflow: hidden;
    box-shadow: 0 6px 18px rgba(0, 0, 0, 0.18);
  }

  /* Back side: contact details */
  .card-back {
    background: var(--card-black);
    color: var(--ink-white);
  }
  .identity {
    position: absolute;
    left: 48px;
    top: 50px;
  }
  .person-name {
    margin: 0;
    font-family: "Jost", sans-serif;
    font-weight: 700;
    font-size: 30px;
    letter-spacing: 0.5px;
    line-height: 1;
    text-transform: uppercase;
  }
  .person-title {
    margin: 6px 0 0;
    font-family: "Cormorant Garamond", serif;
    font-weight: 400;
    font-size: 19px;
    line-height: 1.1;
  }
  .contacts {
    position: absolute;
    left: 48px;
    top: 142px;
    margin: 0;
    padding: 0;
    list-style: none;
    font-family: "Jost", sans-serif;
    font-size: 19px;
    font-weight: 400;
  }
  .contacts li {
    display: flex;
    align-items: center;
    gap: 12px;
    height: 28px;
    white-space: nowrap;
  }
  .contact-icon {
    width: 16px;
    height: 16px;
    flex: none;
  }

  /* Front side: brand over landscape */
  .card-front {
    color: var(--ink-white);
  }
  .landscape {
    position: absolute;
    inset: 0;
    background:
      linear-gradient(var(--photo-shade), var(--photo-shade)),
      radial-gradient(ellipse at 75% 35%, var(--sea-teal) 0%, rgba(31, 138, 140, 0) 60%),
      linear-gradient(160deg, #3f5f5e 0%, #2f5a3a 35%, var(--forest-green) 60%, #1f6e70 100%);
  }
  .brand {
    position: absolute;
    inset: 0;
    display: flex;
    flex-direction: column;
    align-items: center;
    justify-content: center;
    gap: 40px;
    text-align: center;
  }
  .brand-name {
    margin: 0;
    font-family: "Jost", sans-serif;
    font-weight: 600;
    font-size: 34px;
    line-height: 1.1;
    color: var(--ink-white);
  }
  .tagline {
    margin: 0;
    font-family: "Jost", sans-serif;
    font-weight: 600;
    font-size: 18px;
    color: var(--ink-white);
  }
</style>
</head>
<body>
<main class="sheet">
  <section class="card card-back" aria-label="Business card back">
    <div class="identity">
      <h1 class="person-name">Dana Whitcombe</h1>
      <p class="person-title">Chief Executive Officer</p>
    </div>
    <ul class="contacts">
      <li>
        <svg class="contact-icon" viewBox="0 0 24 24" aria-hidden="true">
          <path fill="var(--accent-orange)" d="M6.6 10.8a15.1 15.1 0 0 0 6.6 6.6l2.2-2.2a1 1 0 0 1 1-.25 11.4 11.4 0 0 0 3.6.57 1 1 0 0 1 1 1V20a1 1 0 0 1-1 1A17 17 0 0 1 3 4a1 1 0 0 1 1-1h3.5a1 1 0 0 1 1 1c0 1.25.2 2.45.57 3.6a1 1 0 0 1-.25 1z"/>
        </svg>
        <span>808.555.0147</span>
      </li>
      <li>
        <svg class="contact-icon" viewBox="0 0 24 24" aria-hidden="true">
          <rect x="6" y="2" width="12" height="20" rx="2" fill="none" stroke="var(--accent-orange)" stroke-width="2"/>
          <circle cx="12" cy="18" r="1.2" fill="var(--accent-orange)"/>
        </svg>
        <span>808.555.0198</span>
      </li>
      <li>
        <svg class="contact-icon" viewBox="0 0 24 24" aria-hidden="true">
          <rect x="2" y="5" width="20" height="14" rx="2" fill="none" stroke="var(--accent-orange)" stroke-width="2"/>
          <path d="M3 6l9 7 9-7" fill="none" stroke="var(--accent-orange)" stroke-width="2"/>
        </svg>
        <span>dana@harborlinestaycollective.net</span>
      </li>
      <li>
        <svg class="contact-icon" viewBox="0 0 24 24" aria-hidden="true">
          <circle cx="12" cy="12" r="9.5" fill="none" stroke="var(--accent-orange)" stroke-width="2"/>
          <path d="M2.5 12h19M12 2.5c3 3 3 16 0 19M12 2.5c-3 3-3 16 0 19" fill="none" stroke="var(--accent-orange)" stroke-width="1.6"/>
        </svg>
        <span>www.harborlinestaycollective.net</span>
      </li>
    </ul>
  </section>

  <section class="card card-front" aria-label="Business card front">
    <div class="landscape" role="img" aria-label="Photo of a rocky wooded coastline above turquoise sea"></div>
    <div class="brand">
      <p class="brand-name">Harborline Stay Collective</p>
      <p class="tagline">Luxury Hotel &amp; Resort Email Marketing</p>
    </div>
  </section>
</main>
</body>
</html>
```